SOLVEN TRIDE PORTAL

I'D LIKE TO REDESIGN MY WEBSITE TO MATCH WITH THE NEW BROCHURE WHICH IS ATTACHED. CONTENT AND LOGOS ARE ATTACHED. PLEASE USE WATCH BRAND LOGOS FROM THE BROCHURE
Coded - Design and coding required
1 page

```html
<!DOCTYPE html>
<html lang="en">
<head>
<meta charset="utf-8">
<title>Solven Tride Portal</title>
<link href="https://fonts.googleapis.com/css2?family=Marcellus&family=Mulish:wght@400;600;700&display=swap" rel="stylesheet">
<style>
:root{
  --gold:#c09a3a;
  --gold-dark:#b08a2c;
  --black:#050505;
  --ink:#1a1a1a;
  --white:#ffffff;
  --paper:#fbfaf6;
  --cream:#fcfbe3;
  --cream-box:#f2f0cc;
  --line:#c7b06a;
  --field-border:#d2c48a;
}
*{box-sizing:border-box;margin:0;padding:0}
html,body{width:1200px;height:3486px;overflow:hidden}
body{position:relative;background:var(--paper);font-family:'Mulish',sans-serif;color:var(--ink)}
.abs{position:absolute}
.serif{font-family:'Marcellus',serif}

/* hero */
.hero{left:0;top:0;width:1200px;height:680px;background:radial-gradient(ellipse at 68% 45%,#8a9299 0%,#3a4045 35%,#0d0f11 70%,#050505 100%)}
.hero-photo{left:560px;top:150px;width:560px;height:420px;border-radius:40%;background:radial-gradient(circle at 45% 45%,#2a2d31 0%,#15171a 50%,rgba(20,22,25,0) 72%)}
.brand{display:flex;flex-direction:column;align-items:center;gap:10px}
.brand-mark{width:46px;height:46px;border:2px solid var(--gold)}
.brand-name{font-family:'Marcellus',serif;color:var(--gold);font-size:14px;letter-spacing:1.5px;white-space:nowrap}
.hero .brand{left:120px;top:34px;width:170px}
.nav{display:flex;gap:32px;font-family:'Marcellus',serif;font-size:14px;color:var(--white)}
.nav span{white-space:nowrap}
.hero .nav{right:134px;top:38px}
.nav .active{color:var(--gold);text-decoration:underline;text-underline-offset:4px}
.hero-title{left:127px;top:268px;font-family:'Marcellus',serif;font-size:52px;line-height:66px;color:var(--white)}
.dots{left:568px;top:619px;display:flex;gap:5px}
.dots i{width:11px;height:11px;border:1.5px solid var(--white);border-radius:50%}
.dots i.on{background:var(--gold);border-color:var(--gold)}
.torn{left:0;width:1200px}

/* welcome */
.welcome-photo{left:218px;top:737px;width:252px;height:415px;border-radius:60px;background:linear-gradient(180deg,#2e4a7a 0%,#c8cdd3 30%,#7f8c9e 55%,#2f4b7b 100%)}
.kicker{left:602px;top:762px;font-family:'Marcellus',serif;font-size:21px;color:var(--ink)}
.section-title{font-family:'Marcellus',serif;font-size:32px;color:var(--gold);white-space:nowrap}
.welcome-title{left:602px;top:790px}
.rule{height:2px;width:80px;background:var(--gold)}
.subhead{left:601px;top:884px;font-size:19px;color:var(--ink)}
.body-copy{font-size:14px;line-height:21px}
.welcome-copy{left:602px;top:925px;width:410px;color:#333}
.welcome-copy p+p{margin-top:24px}

/* about */
.about{left:0;top:1197px;width:1200px;height:558px;background:var(--black)}
.about-photo{left:580px;top:0;width:620px;height:558px;background:radial-gradient(circle at 52% 52%,#34373b 0%,#1a1b1d 40%,#080808 70%,#050505 100%)}
.about-title{left:130px;top:50px}
.about-copy{left:130px;top:140px;width:440px;color:var(--white);text-align:justify}
.about-copy p+p{margin-top:21px}

/* investments */
.invest-box{left:227px;top:1832px;width:746px;height:180px;border:1.5px solid var(--line)}
.invest-title{left:0;top:1810px;width:1200px;text-align:center}
.invest-title span{background:var(--paper);padding:0 14px}
.invest-copy{left:380px;top:1900px;width:440px;text-align:center;color:#333}

/* sourcing */
.sourcing{left:0;top:2073px;width:1200px;height:532px;background:radial-gradient(ellipse at 58% 50%,#1d2422 0%,#0c0f0e 45%,#030303 80%)}
.centre-title{left:0;width:1200px;text-align:center}
.field{background:var(--white);font-size:12px;color:#333;padding:14px 14px}
.field.cream{border:1px solid var(--field-border);background:var(--white)}
.select::after{content:"";position:absolute;right:12px;top:18px;border:4px solid transparent;border-top:5px solid #222}
.btn{background:var(--gold);color:var(--white);font-size:20px;display:flex;align-items:center;justify-content:center}

/* contact */
.contact{left:0;top:2605px;width:1200px;height:580px;background:var(--cream)}
.icon{width:30px;height:30px}
.divider{width:1px;height:42px;background:#bbb}
.label{font-size:14px;color:var(--ink)}
.value{font-size:20px;font-weight:700;color:var(--gold)}
.note{left:130px;top:2931px;width:384px;height:137px;background:var(--cream-box);padding:30px 40px;font-size:16px;line-height:22px;color:#222}
.note b{color:var(--gold)}

/* footer */
.footer{left:0;top:3170px;width:1200px;height:316px;background:var(--black)}
.footer .brand{left:0;top:48px;width:1200px}
.footer .nav{left:0;top:206px;width:1200px;justify-content:center}
.copyright{left:0;top:250px;width:1200px;text-align:center;font-size:12px;color:var(--white)}
</style>
</head>
<body>

<section class="abs hero">
  <div class="abs hero-photo" role="img" aria-label="Dark dive watch with black bezel resting on a wet reflective surface"></div>
  <div class="abs brand"><div class="brand-mark"></div><div class="brand-name">SOLVEN TRIDE PORTAL</div></div>
  <nav class="abs nav"><span class="active">HOME</span><span>ABOUT</span><span>INVESTMENTS</span><span>SEARCH WATCHES</span><span>CONTACT</span></nav>
  <h1 class="abs hero-title">SOLVEN TRIDE<br>PORTAL</h1>
  <div class="abs dots"><i></i><i class="on"></i><i></i><i></i></div>
</section>
<svg class="abs torn" style="top:664px" height="36" viewBox="0 0 1200 36" preserveAspectRatio="none" aria-hidden="true">
  <polygon fill="#050505" points="0,0 1200,0 1200,10 1150,12 1100,8 1040,14 980,9 900,15 840,10 760,13 700,8 620,14 540,9 470,13 400,8 330,15 260,10 190,14 120,9 60,18 20,12 0,20"/>
</svg>

<div class="abs welcome-photo" role="img" aria-label="Steel chronograph wristwatch with blue dial and blue rubber strap"></div>
<p class="abs kicker">Welcome to</p>
<h2 class="abs section-title welcome-title">Solven Tride Portal</h2>
<div class="abs rule" style="left:602px;top:847px"></div>
<h3 class="abs subhead">International luxury timepiece supplier</h3>
<div class="abs body-copy welcome-copy">
  <p>Simply choose a desired product and allow us to source it for you at the best price and with suitable delivery terms. You will have an option to either collect your purchase from our Ashfield based boutique store, collection points are also in New York City or Dubai or get it delivered to your door via one of our fully insured couriers.</p>
  <p>Making your luxury shopping experience as simple as<br>it can be.</p>
</div>

<section class="abs about">
  <div class="abs about-photo" role="img" aria-label="Black chronograph watch with yellow hands on a dark leather strap"></div>
  <h2 class="abs section-title about-title">About us</h2>
  <div class="abs rule" style="left:130px;top:100px"></div>
  <div class="abs body-copy about-copy">
    <p>Solven Tride Portal was first founded in 2018, it has been established as the premier resource to buy and sell premium pre-owned watches. With thousands of watches available from brands including Corvane, Halden Moreau, Varenne Lisle, Aurel Stahl, Ostrel, Belmaine and more, plus international locations and clients there's no better place to find a luxury timepiece.</p>
    <p>Outstanding customer service is a mainstay of the Solven Tride ethos. Watch collectors are discerning shoppers, and will accept nothing but the best, which is why customer service has and always will be such an important part of the business.</p>
    <p>Our dedicated team of swiss watch experts are perfectly placed to adapt to the ever changing market conditions, giving our investors an 'out of the box' solution. Longevity is as much a focus as immediate success, ensuring you have the best options we can provide tomorrow as well as</p>
  </div>
</section>

<div class="abs invest-box"></div>
<h2 class="abs section-title invest-title"><span>Investments</span></h2>
<div class="abs rule" style="left:587px;top:1864px;width:26px"></div>
<p class="abs body-copy invest-copy">Interested in becoming part of the ever growing Solven Tride Portal? &nbsp;Please leave your details contact form below and one of the team will be in touch to discuss potential options.</p>

<section class="abs sourcing" role="img" aria-label="Close-up of a dark watch dial with luminous numerals">
</section>
<h2 class="abs section-title centre-title" style="top:2122px">Sourcing your watch</h2>
<div class="abs rule" style="left:587px;top:2190px;width:26px"></div>
<div class="abs field" style="left:271px;top:2236px;width:217px;height:42px">Watch brand</div>
<div class="abs field select" style="left:500px;top:2236px;width:216px;height:42px">Year</div>
<div class="abs field" style="left:726px;top:2236px;width:216px;height:42px">Material</div>
<div class="abs field" style="left:271px;top:2290px;width:329px;height:42px">Bezel</div>
<div class="abs field" style="left:613px;top:2290px;width:330px;height:42px">Strap</div>
<div class="abs field" style="left:271px;top:2345px;width:672px;height:120px">Description</div>
<div class="abs btn" style="left:541px;top:2501px;width:118px;height:47px">Submit</div>

<section class="abs contact"></section>
<h2 class="abs section-title centre-title" style="top:2642px">Contact Us</h2>
<div class="abs rule" style="left:587px;top:2703px;width:26px"></div>

<svg class="abs icon" style="left:139px;top:2780px" viewBox="0 0 24 24" aria-hidden="true"><path fill="#c09a3a" d="M6.6 10.8a15.1 15.1 0 0 0 6.6 6.6l2.2-2.2c.3-.3.7-.4 1-.2 1.1.4 2.3.6 3.6.6.6 0 1 .4 1 1V20c0 .6-.4 1-1 1A17 17 0 0 1 3 4c0-.6.4-1 1-1h3.5c.6 0 1 .4 1 1 0 1.3.2 2.5.6 3.6.1.3 0 .7-.2 1z"/></svg>
<div class="abs divider" style="left:183px;top:2774px"></div>
<p class="abs label" style="left:204px;top:2767px">Call us</p>
<p class="abs value" style="left:204px;top:2786px">01632 960 418</p>

<svg class="abs icon" style="left:139px;top:2855px" viewBox="0 0 24 24" aria-hidden="true"><rect x="3" y="5" width="18" height="14" rx="1.5" fill="none" stroke="#c09a3a" stroke-width="2"/><path d="M3.5 6l8.5 7 8.5-7" fill="none" stroke="#c09a3a" stroke-width="2"/></svg>
<div class="abs divider" style="left:183px;top:2850px"></div>
<p class="abs label" style="left:204px;top:2844px">Email us</p>
<p class="abs value" style="left:204px;top:2864px">sales@solventride-portal.co.uk</p>

<div class="abs note">Alternatively please feel free to contact us on <b>01632 960 418</b> &nbsp;For a more detailed chat with one of our timepiece specialists</div>

<div class="abs field cream" style="left:553px;top:2764px;width:252px;height:42px">First Name</div>
<div class="abs field cream" style="left:817px;top:2764px;width:251px;height:42px">Last Name</div>
<div class="abs field cream" style="left:553px;top:2821px;width:252px;height:42px">Phone Number</div>
<div class="abs field cream" style="left:817px;top:2821px;width:251px;height:42px">Email</div>
<div class="abs field cream" style="left:553px;top:2879px;width:515px;height:121px">Message</div>
<div class="abs btn" style="left:553px;top:3018px;width:136px;height:46px">Submit</div>

<svg class="abs torn" style="top:3148px" height="24" viewBox="0 0 1200 24" preserveAspectRatio="none" aria-hidden="true">
  <polygon fill="#050505" points="0,10 40,6 90,12 150,4 230,11 300,7 380,13 460,6 540,12 620,5 700,11 780,7 860,13 940,5 1020,11 1100,6 1160,12 1200,8 1200,24 0,24"/>
</svg>
<footer class="abs footer">
  <div class="abs brand"><div class="brand-mark"></div><div class="brand-name" style="font-size:15px">SOLVEN TRIDE PORTAL</div></div>
  <nav class="abs nav"><span>HOME</span><span>ABOUT</span><span>INVESTMENTS</span><span>SEARCH WATCHES</span><span>CONTACT</span></nav>
  <p class="abs copyright">Copyright © 2022 All Rights Reserved</p>
</footer>

</body>
</html>
```